Personal Finance e-commerce website needs a simple budget design

Hello! I am starting to sell downloadable and printable budget planners, as shown in the attached file, for people to plan ahead on their personal finances. <br/><br/>I want to see a one-page design with similar columns (for example, "Expenses, Budget, and Actual"). I would also like to see the basic formula ("Net Income = Gross income - Total Expenses") somewhere on the design. Finally, I want the design to remain mostly minimalistic and simple for the average person to plan their personal monthly budgets.<br/><br/>However, other than that, the overall design, layout, and colors will be at the graphic designer's choice. If you have any questions for me, please let me know. Thank you for your time!

Industry/Entity Type

Financial Planning

Colors

Designer to choose colors to be used in the design.

Requirements
Must have
• I want to see a one-page design with similar columns (for example, "Expenses, Budget, and Actual").
• I want the design to remain mostly minimalistic and simple for the average person to plan their personal monthly budgets.
Nice to have
• I would also like to see the basic formula ("Net Income = Gross income - Total Expenses") somewhere on the design.

```html
<!DOCTYPE html>
<html lang="en">
<head>
<meta charset="utf-8">
<title>Basic Monthly Budget – Marlow Finch</title>
<link rel="stylesheet" href="https://fonts.googleapis.com/css2?family=Arimo:wght@700&family=Catamaran:wght@400&family=Montserrat:wght@800&display=swap">
<style>
  :root {
    --brand-purple: #93278f;
    --ink: #000000;
    --header-gold: #cbac6a;
    --pill-green: #066b3a;
    --caption-grey: #555555;
    --rail-mint: #dce8e0;
    --dash-sage: #b5c6b5;
    --formula-navy: #0c3442;
    --paper: #ffffff;
  }
  * { margin: 0; padding: 0; box-sizing: border-box; }
  html, body { width: 927px; height: 1200px; overflow: hidden; background: var(--paper); }
  .sheet { position: relative; width: 927px; height: 1200px; font-family: "Arimo", Arial, sans-serif; color: var(--ink); }

  .brand { position: absolute; left: 31px; top: 34px; width: 275px; height: 126px; display: flex; flex-direction: column; justify-content: center; padding-left: 24px; }
  .brand-name { font-family: "Montserrat", sans-serif; font-weight: 800; font-size: 46px; line-height: 1.05; letter-spacing: 3px; color: var(--brand-purple); }

  .title { position: absolute; left: 338px; top: 66px; font-size: 51px; font-weight: 700; letter-spacing: 0.5px; white-space: nowrap; }
  .period { position: absolute; left: 421px; top: 146px; font-size: 27px; font-weight: 700; white-space: nowrap; }
  .period .blank { display: inline-block; width: 137px; border-bottom: 3px solid var(--ink); margin-right: 1px; }

  .col-head { position: absolute; top: 203px; height: 144px; background: var(--header-gold); text-align: center; }
  .col-head.expenses { left: 43px; width: 334px; }
  .col-head.budget { left: 391px; width: 239px; }
  .col-head.actual { left: 643px; width: 232px; }
  .pill { position: absolute; top: 13px; height: 41px; border-radius: 21px; background: var(--pill-green); color: var(--paper);
          font-family: "Montserrat", sans-serif; font-weight: 800; font-size: 33px; line-height: 41px; letter-spacing: 2px; white-space: nowrap; }
  .expenses .pill { left: 43px; width: 231px; }
  .budget .pill { left: 8px; width: 223px; }
  .actual .pill { left: 11px; width: 218px; letter-spacing: 1.5px; }
  .caption { position: absolute; left: 0; right: 0; top: 62px; font-family: "Catamaran", sans-serif; font-size: 28px; line-height: 33px; color: var(--caption-grey); }

  .grid { position: absolute; left: 0; top: 347px; }

  .formula { position: absolute; left: 29px; top: 1020px; width: 860px; height: 114px; border-radius: 22px; background: var(--formula-navy);
             color: var(--paper); font-size: 36px; font-weight: 700; text-align: center; line-height: 114px; white-space: pre; }
  .footer { position: absolute; left: 0; width: 927px; top: 1143px; text-align: center; font-size: 21px; font-weight: 700; }
  .footer .link { color: var(--brand-purple); }
</style>
</head>
<body>
<main class="sheet">
  <div class="brand"><span class="brand-name">MARLOW<br>FINCH</span></div>

  <h1 class="title">Basic Monthly BUDGET</h1>
  <p class="period">Month<span class="blank"></span>Year<span class="blank"></span></p>

  <section class="col-head expenses"><span class="pill">EXPENSES</span><p class="caption">Custom Category</p></section>
  <section class="col-head budget"><span class="pill">BUDGET ($)</span><p class="caption">What You Plan<br>to spend</p></section>
  <section class="col-head actual"><span class="pill">ACTUAL ($)</span><p class="caption">What You Actually<br>spend</p></section>

  <svg class="grid" width="927" height="650" viewBox="0 347 927 650" aria-label="Budget entry rows">
    <defs>
      <g id="rails">
        <rect x="29" width="14" fill="var(--rail-mint)" height="100%"/>
      </g>
    </defs>
    <g fill="var(--rail-mint)">
      <!-- rails per row: y, height -->
      <g id="r1"><rect x="29" y="347" width="14" height="71"/><rect x="377" y="347" width="14" height="71"/><rect x="630" y="347" width="14" height="71"/><rect x="875" y="347" width="14" height="71"/></g>
      <rect x="29" y="436" width="14" height="62"/><rect x="377" y="436" width="14" height="62"/><rect x="630" y="436" width="14" height="62"/><rect x="875" y="436" width="14" height="62"/>
      <rect x="29" y="516" width="14" height="68"/><rect x="377" y="516" width="14" height="68"/><rect x="630" y="516" width="14" height="68"/><rect x="875" y="516" width="14" height="68"/>
      <rect x="29" y="602" width="14" height="60"/><rect x="377" y="602" width="14" height="60"/><rect x="630" y="602" width="14" height="60"/><rect x="875" y="602" width="14" height="60"/>
      <rect x="29" y="681" width="14" height="61"/><rect x="377" y="681" width="14" height="61"/><rect x="630" y="681" width="14" height="61"/><rect x="875" y="681" width="14" height="61"/>
      <rect x="29" y="760" width="14" height="59"/><rect x="377" y="760" width="14" height="59"/><rect x="630" y="760" width="14" height="59"/><rect x="875" y="760" width="14" height="59"/>
      <rect x="29" y="837" width="14" height="65"/><rect x="377" y="837" width="14" height="65"/><rect x="630" y="837" width="14" height="65"/><rect x="875" y="837" width="14" height="65"/>
      <rect x="29" y="920" width="14" height="63"/><rect x="377" y="920" width="14" height="63"/><rect x="630" y="920" width="14" height="63"/><rect x="875" y="920" width="14" height="63"/>
    </g>
    <g stroke="var(--dash-sage)" stroke-width="5" stroke-dasharray="13 16">
      <path d="M52 425H362M403 425H625M651 425H872"/>
      <path d="M52 508H362M403 508H625M651 508H872"/>
      <path d="M52 590H362M403 590H625M651 590H872"/>
      <path d="M52 669H362M403 669H625M651 669H872"/>
      <path d="M52 748H362M403 748H625M651 748H872"/>
      <path d="M52 826H362M403 826H625M651 826H872"/>
      <path d="M52 911H362M403 911H625M651 911H872"/>
      <path d="M52 988H362M403 988H625M651 988H872"/>
    </g>
  </svg>

  <div class="formula">Net Income = Gross Income - Total  Expenses</div>
  <p class="footer">visit us at <span class="link">www.marlowfinch.com</span> for personal financial advice!</p>
</main>
</body>
</html>
```